Business Cards Needed For Veterinary Business

Looking for a business card design for a veterinary blood bank. We would like it to be clean and professional on appearance but still warm and inviting. We would like to utilize our logo and similar coloring. We will use our phone number, email, website, employee name, employee title.

We do not want a bunch of animated animal photos but do not need the style to be as clinical as a laboratory or human medical procedure office.

We are looking for some creative ideas to choose from so that we can generate a standout professional business card for our management team to utilize.

Target Market(s)

professionals

Industry/Entity Type

veterinary

Contact Information for Business Card

employee name, employee title, phone number, website URL, email

Font styles to use
Sans Serif

Colors
0054AA
0677BA
7BADD7
CADEEF
E8F1F8
EB3D1F
EC4F4E
F09395
F8D3D4
FCEDEE

Requirements
Nice to have
• creative design
Should not have
• animated photos

```html
<!DOCTYPE html>
<html lang="en">
<head>
<meta charset="utf-8">
<title>Harbor Veterinary Blood Bank – Business Cards</title>
<link rel="stylesheet" href="https://fonts.googleapis.com/css2?family=Montserrat:wght@700;800&family=Roboto:wght@400;500;700&display=swap">
<style>
  :root {
    --backdrop: #262626;
    --card: #f1f1f1;
    --red: #d7192a;
    --red-deep: #c8102e;
    --blue: #11468f;
    --purple: #5a2f6e;
    --ink: #2e2e2e;
    --white: #ffffff;
  }
  * { box-sizing: border-box; margin: 0; padding: 0; }
  html, body {
    width: 1200px; height: 576px; overflow: hidden;
    background: var(--backdrop);
  }
  .stage { position: relative; width: 1200px; height: 576px; }
  .card {
    position: absolute;
    background: var(--card);
    border-radius: 9px;
    overflow: hidden;
    box-shadow: 0 4px 14px rgba(0,0,0,.45);
  }
  .card--front { left: 102px; top: 139px; width: 484px; height: 292px; }
  .card--back  { left: 596px; top: 138px; width: 480px; height: 291px; }

  /* front */
  .brand {
    position: absolute; display: flex; align-items: center; gap: 12px;
  }
  .brand__dot {
    width: 46px; height: 46px; border-radius: 50%; background: var(--red); flex: none;
  }
  .brand__name {
    font-family: "Montserrat", sans-serif; font-weight: 800;
    color: var(--red); text-transform: uppercase; line-height: 1.05;
  }
  .card--front .brand { left: 80px; top: 80px; }
  .card--front .brand__name { font-size: 25px; }
  .front-web {
    position: absolute; left: 0; right: 0; top: 236px;
    display: flex; align-items: center; justify-content: center; gap: 12px;
    font-family: "Roboto", sans-serif; font-size: 13px; color: var(--ink);
  }
  .front-web__rule { width: 54px; height: 2px; background: var(--red); }
  .front-band { position: absolute; left: 0; bottom: 0; width: 100%; height: 19px; }

  /* back */
  .back-wave { position: absolute; left: 0; top: 0; width: 480px; height: 120px; }
  .person {
    position: absolute; right: 23px; top: 20px; text-align: right;
    font-family: "Roboto", sans-serif; color: var(--white);
  }
  .person__name { font-size: 18px; font-weight: 500; }
  .person__title { font-size: 12px; margin-top: 4px; }
  .card--back .brand { left: 20px; top: 108px; }
  .card--back .brand__name { font-size: 24px; }
  .contacts {
    position: absolute; left: 17px; top: 206px; list-style: none;
    font-family: "Roboto", sans-serif; font-size: 13px; color: var(--ink);
  }
  .contacts li { display: flex; align-items: center; gap: 12px; height: 19px; }
  .contacts svg { width: 13px; height: 11px; fill: var(--red); }
  .contacts .address { gap: 0; }
  .emblem {
    position: absolute; left: 332px; top: 118px; width: 118px; height: 118px;
    border-radius: 50%; background: var(--red);
  }
</style>
</head>
<body>
<main class="stage">

  <section class="card card--front">
    <div class="brand">
      <span class="brand__dot"></span>
      <span class="brand__name">Harbor Veterinary<br>Blood Bank</span>
    </div>
    <div class="front-web">
      <span class="front-web__rule"></span>
      <span>www.harborbloodbank.com</span>
      <span class="front-web__rule"></span>
    </div>
    <svg class="front-band" viewBox="0 0 484 19" preserveAspectRatio="none">
      <polygon points="0,0 240,0 226,19 0,19" fill="var(--blue)"/>
      <polygon points="244,0 484,0 484,19 230,19" fill="var(--red-deep)"/>
    </svg>
  </section>

  <section class="card card--back">
    <svg class="back-wave" viewBox="0 0 480 120">
      <defs>
        <linearGradient id="waveFill" x1="0" y1="0" x2="1" y2="0">
          <stop offset="0" stop-color="var(--blue)"/>
          <stop offset=".45" stop-color="var(--purple)"/>
          <stop offset="1" stop-color="var(--red)"/>
        </linearGradient>
      </defs>
      <path d="M0 0H480V80C390 80 320 14 190 14C110 14 50 28 0 42Z" fill="url(#waveFill)"/>
      <path d="M0 52C60 30 150 20 230 28C330 38 380 94 480 84V94C380 104 320 50 230 40C150 33 60 44 0 64Z" fill="var(--red)"/>
      <path d="M0 72C70 50 160 44 240 52C330 62 390 112 480 100V108C390 120 330 72 240 62C160 55 70 62 0 80Z" fill="var(--blue)"/>
    </svg>
    <div class="person">
      <div class="person__name">Jordan Ellis</div>
      <div class="person__title">Managing Director</div>
    </div>
    <div class="brand">
      <span class="brand__name">Harbor Veterinary<br>Blood Bank</span>
    </div>
    <div class="emblem" role="img" aria-label="Blood bank emblem area"></div>
    <ul class="contacts">
      <li><svg viewBox="0 0 13 11"><path d="M1 3C1 1 3 0 6.5 0S12 1 12 3H9.5V2H3.5V3ZM3 4H10L12 9V11H1V9ZM6.5 5.5A1.7 1.7 0 1 0 6.5 8.9A1.7 1.7 0 1 0 6.5 5.5Z"/></svg>555-014-2290</li>
      <li><svg viewBox="0 0 13 11"><path d="M0 1H13V2L6.5 6L0 2ZM0 3.5L6.5 7.5L13 3.5V10H0Z"/></svg>jordan@harborbloodbank.com</li>
      <li><svg viewBox="0 0 13 11"><circle cx="6.5" cy="5.5" r="5" fill="none" stroke="var(--red)" stroke-width="1.4"/><path d="M1.5 5H11.5V6H1.5ZM6 0.5H7V10.5H6Z"/></svg>www.harborbloodbank.com</li>
      <li class="address">58 Maple Row, Fairview, US 10482</li>
    </ul>
  </section>

</main>
</body>
</html>
```